Business Card Design

Just looking for a good designs that looks good with our company logo. I'd like it to be simple and to the point. Just including contact information, our logo, and my name somewhere on the card so future clients know who they're contacting, and a couple services offered. The two images I attached are pictures of our logo. I don't care which color they they are, I just attached both images to give a reference of logo colors depending on the color of the card.
Names: Calvin Prewitt
Phone: 555-247-9061
Email: tidyturfcrew@mailvista.net
Services offered:
Mowing
Fertilization
Aeration
Bed & tree maintenance
and more.
Industry/Entity Type
Business
Contact Information for Business Card
Names: Calvin Prewitt
Phone: 555-247-9061
Look and feel

```html
<!DOCTYPE html>
<html lang="en">
<head>
<meta charset="utf-8">
<title>Tidy Turf – Business Card</title>
<link rel="stylesheet" href="https://fonts.googleapis.com/css2?family=Montserrat:wght@300;400;500;600&display=swap">
<style>
  :root {
    --backdrop: #e7e4e0;
    --card: #f7f7f7;
    --card-shade: #e9e9e9;
    --brand-red: #d8513c;
    --brand-peach: #efc1ab;
    --ink: #2b2b2e;
    --ink-soft: #5a4a46;
    --white: #ffffff;
  }
  * { box-sizing: border-box; margin: 0; padding: 0; }
  html, body {
    width: 1200px;
    height: 724px;
    overflow: hidden;
    background: var(--backdrop);
    font-family: "Montserrat", sans-serif;
  }
  .canvas {
    position: relative;
    width: 1200px;
    height: 724px;
    display: flex;
    align-items: center;
    justify-content: center;
  }
  .business-card {
    position: relative;
    width: 380px;
    height: 664px;
    background: linear-gradient(160deg, var(--white) 0%, var(--card) 55%, var(--card-shade) 100%);
    box-shadow: 0 10px 30px rgba(0,0,0,0.18);
    overflow: hidden;
  }
  .card-shapes {
    position: absolute;
    inset: 0;
    width: 100%;
    height: 100%;
  }
  .shape-ring { fill: var(--brand-peach); }
  .shape-red { fill: var(--brand-red); }
  .shape-notch { fill: var(--card); }

  .brand {
    position: absolute;
    top: 110px;
    left: 0;
    right: 0;
    display: flex;
    justify-content: center;
    align-items: center;
    gap: 10px;
  }
  .brand-dot {
    width: 22px;
    height: 22px;
    border-radius: 50%;
    background: var(--brand-red);
  }
  .brand-name {
    font-weight: 600;
    font-size: 26px;
    letter-spacing: 1px;
    color: var(--ink);
  }

  .services {
    position: absolute;
    top: 158px;
    left: 40px;
    right: 40px;
    text-align: center;
    font-weight: 400;
    font-size: 12px;
    line-height: 1.7;
    letter-spacing: 0.4px;
    color: var(--ink-soft);
  }

  .person-name {
    position: absolute;
    top: 400px;
    left: 118px;
    font-size: 26px;
    line-height: 1;
    white-space: nowrap;
  }
  .name-first {
    font-weight: 300;
    color: var(--ink-soft);
  }
  .name-last {
    font-weight: 500;
    color: var(--ink);
    letter-spacing: 0.5px;
  }

  .contact {
    position: absolute;
    left: 36px;
    color: var(--white);
    font-weight: 500;
    letter-spacing: 0.5px;
  }
  .contact-phone {
    top: 520px;
    display: flex;
    align-items: center;
    gap: 12px;
    font-size: 18px;
  }
  .contact-email {
    top: 566px;
    font-size: 13px;
    font-weight: 400;
  }
  .phone-icon {
    width: 26px;
    height: 26px;
  }
</style>
</head>
<body>
<main class="canvas">
  <article class="business-card">
    <svg class="card-shapes" viewBox="0 0 380 664" aria-hidden="true">
      <circle class="shape-ring" cx="70" cy="480" r="228"/>
      <circle class="shape-red" cx="70" cy="480" r="210"/>
      <circle class="shape-notch" cx="318" cy="440" r="118"/>
    </svg>

    <div class="brand">
      <span class="brand-dot"></span>
      <span class="brand-name">TIDY TURF</span>
    </div>

    <p class="services">Mowing · Fertilization · Aeration<br>Bed &amp; tree maintenance · and more</p>

    <p class="person-name"><span class="name-first">calvin</span> <span class="name-last">PREWITT</span></p>

    <p class="contact contact-phone">
      <svg class="phone-icon" viewBox="0 0 26 26" aria-hidden="true">
        <circle cx="13" cy="13" r="13" fill="#ffffff"/>
        <path d="M9.2 7.2c.5-.4 1.1-.3 1.4.2l1.2 2c.3.5.2 1-.2 1.4l-.8.7c.6 1.4 1.7 2.6 3.1 3.3l.7-.8c.4-.4 1-.5 1.4-.2l2 1.2c.5.3.6.9.2 1.4l-.9 1.1c-.5.6-1.3.8-2 .5-3.4-1.3-6-3.9-7.3-7.3-.3-.7-.1-1.5.5-2z" fill="#d8513c"/>
      </svg>
      <span class="phone-number">555-247-9061</span>
    </p>
    <p class="contact contact-email">tidyturfcrew@mailvista.net</p>
  </article>
</main>
</body>
</html>
```